Visitenkarten-Design für Landschaftspfleger
Es waren viele tolle Designer am Werk, dieser zeichnet sich durch optimal Umsetzung der Aufgabenstellung aus - und hat von Anfang an meinen Stil getroffen...
Zielgruppe
Wir sind Landschaftspfleger kritischer Infrastruktur. Unsere Zielgruppe ist das operativer Management Großer Energiekonzerne die den Einkauf managen, Ausschreibungen und Vergabemaßnahmen organisieren.
Aufgabenstellung
Die Designs sollen nur die Logofarben enthalten, Weniger ist mehr.
Slogan:
Moderne Trassenpflege erhält LEBENSRÄUME!
Adresse: Lindenhofweg 12
15748 Märkisch Buchholz
Julian Krammel
MBA Agrarmanagement
Projektleiter Trassen- / Stationspflege
Telefon:01609348271
mail: julian.krammel@velorit-beispiel.de
www.velorit-beispiel.de

```html
<!DOCTYPE html>
<html lang="de">
<head>
<meta charset="utf-8">
<title>Visitenkarte – Julian Krammel</title>
<link rel="stylesheet" href="https://fonts.googleapis.com/css2?family=Source+Serif+4:opsz,wght@8..60,500;8..60,600&family=Inter:wght@400;500&display=swap">
<style>
  :root {
    --backdrop: #dedbd6;
    --card: #eae8e3;
    --relief-light: #f1efeb;
    --relief-dark: #dcd9d3;
    --ink: #3a3936;
    --ink-soft: #5a5954;
    --olive: #6f7a45;
  }
  * { margin: 0; padding: 0; box-sizing: border-box; }
  html, body {
    width: 1200px; height: 900px; overflow: hidden;
    background: var(--backdrop);
  }
  .canvas { position: relative; width: 1200px; height: 900px; }
  .card {
    position: absolute; top: 316px;
    width: 508px; height: 268px;
    background: var(--card);
    overflow: hidden;
  }
  .card--front { left: 62px; }
  .card--back { left: 630px; }
  .relief {
    position: absolute;
    background: linear-gradient(135deg, var(--relief-light) 0%, var(--relief-dark) 55%, var(--relief-light) 100%);
    opacity: 0.7;
  }
  .card--front .relief { left: 292px; top: 78px; width: 216px; height: 190px; }
  .card--back .relief { left: 0; top: 78px; width: 508px; height: 190px; }
  .holder-name {
    position: absolute; left: 24px; top: 2px;
    font-family: "Source Serif 4", Georgia, serif;
    font-weight: 600; font-size: 60px; line-height: 0.93;
    letter-spacing: -1px; color: var(--ink);
  }
  .holder-role {
    position: absolute; left: 23px; top: 138px;
    font-family: "Inter", Arial, sans-serif;
    font-size: 26px; line-height: 1.3; color: var(--olive);
  }
  .contact {
    position: absolute; left: 24px; top: 216px;
    font-family: "Inter", Arial, sans-serif;
    font-size: 12.5px; line-height: 1.5; color: var(--ink-soft);
    list-style: none;
  }
  .tagline {
    position: absolute; left: 30px; top: 88px;
    font-family: "Inter", Arial, sans-serif;
    font-weight: 500; font-size: 35px; line-height: 1.2;
    letter-spacing: 0.5px; color: var(--ink);
  }
  .slogan {
    position: absolute; left: 31px; top: 200px;
    font-family: "Inter", Arial, sans-serif;
    font-size: 15px; line-height: 1.3; color: var(--olive);
  }
  .website {
    position: absolute; left: 31px; top: 224px;
    font-family: "Inter", Arial, sans-serif;
    font-size: 13px; line-height: 1.3; color: var(--ink-soft);
  }
</style>
</head>
<body>
  <main class="canvas">
    <section class="card card--front">
      <div class="relief" role="img" aria-label="Blindgeprägtes Linienmuster aus geschwungenen Feldfurchen"></div>
      <h1 class="holder-name">Julian<br>Krammel</h1>
      <p class="holder-role">MBA Agrarmanagement –<br>Project Lead</p>
      <ul class="contact">
        <li>Lindenhofweg 12 · 15748 Märkisch Buchholz</li>
        <li>01609348271 · julian.krammel@velorit-beispiel.de</li>
      </ul>
    </section>
    <section class="card card--back">
      <div class="relief" role="img" aria-label="Blindgeprägtes Linienmuster aus geschwungenen Feldfurchen"></div>
      <p class="tagline">SUSTAINABLE<br>LEADERSHIP</p>
      <p class="slogan">Moderne Trassenpflege erhält LEBENSRÄUME!</p>
      <p class="website">www.velorit-beispiel.de</p>
    </section>
  </main>
</body>
</html>
```